Label Redesign For Hemp Oil Tincture Bottle*

I need a label redesigned for Marbleleaf Hemp, current bottle label and logo is attached. The current label doesn't standout, not sure if its the font size or colors on the existing label. It is very important to have on the label that this is a Premium Full Spectrum Hemp Oil that is 2000mg. Then after the label is redesigned and approved, I would need to packaging to be designed to match the approved label design.
This Hemp oil has a relaxing effect to help ease mental and emotional stress, tension and worry. The Omega Fatty Acids it contains also naturally improves your mood and overall brain function, causing you to feel more alert and focused. Hemp Oil helps with insomnia. Take some 2-3 hours before bedtime, you will feel relaxed yet aware of how tired you are that it will lead to a good night's sleep. Hemp Oil helps ease chronic pain and inflammation from conditions such as arthritis, fibromyalgia, lupus, and MS. As a pain relief supplement, it is a safer, natural, non-chemical and non-addictive alternative to prescription painkillers.

Target Market(s)

Adults

Industry/Entity Type

Supplement

Font styles to use
Serif
Sans Serif

Colors

Designer to choose colors to be used in the design.

Requirements
Must have
• All information thats on current label but where it says 750 in the front of the existing label, it needs to say 2000. The 2000 should be prominent on the label.

```html
<!DOCTYPE html>
<html lang="en">
<head>
<meta charset="utf-8">
<title>Marbleleaf Hemp – Label Proof</title>
<link rel="stylesheet" href="https://fonts.googleapis.com/css2?family=Inter:wght@600&family=Jost:wght@300;400;500&family=Roboto+Condensed:wght@300;400;700&display=swap">
<style>
  :root{
    --paper:#ffffff;
    --label-bg:#231f20;
    --pill:#5a5a5a;
    --pill-text:#1f1c1d;
    --ink:#ffffff;
    --muted:#6f6f6f;
    --brand-green:#8cc63f;
    --silver:#bdbdbd;
    --rule:#d9d9d9;
    --pink:#e6007e;
    --cyan:#00aeef;
    --caption:#1a1a1a;
  }
  *{box-sizing:border-box;margin:0;padding:0}
  html,body{width:1200px;height:1200px;overflow:hidden;background:var(--paper)}
  .sheet{position:relative;width:1200px;height:1200px;font-family:"Jost",sans-serif}

  .row-caption{position:absolute;font-family:"Inter",sans-serif;font-weight:600;color:var(--caption);font-size:19px;line-height:25px;text-align:center}
  .divider{position:absolute;left:27px;width:1140px;height:1px;background:var(--rule)}
  .note{position:absolute;font-family:"Roboto Condensed",sans-serif;font-weight:300;font-size:17px;line-height:24px;text-align:center}
  .note--silver{color:var(--pink)}
  .note--white{color:var(--cyan)}
  .pointer{position:absolute;left:0;top:0;overflow:visible}

  .label{position:absolute;width:692px;height:307px;background:var(--label-bg);color:var(--ink);box-shadow:6px 8px 10px rgba(0,0,0,.35)}
  .label--white{background:var(--paper);box-shadow:6px 8px 10px rgba(0,0,0,.3)}
  .label > *{position:absolute}
  .col-left{left:0;width:228px;text-align:center}
  .col-center{left:246px;width:200px;text-align:center}
  .pill{display:inline-block;background:var(--pill);color:var(--pill-text);border-radius:5px;padding:0 6px;font-size:13px;line-height:16px;font-weight:400}
  .pill--strong{color:var(--ink);font-weight:500;font-size:12.5px;line-height:19px;padding:0 6px}
  .body-copy{font-size:10px;line-height:15.4px;font-weight:300;letter-spacing:-.2px}
  .caps{font-size:12.5px;line-height:19px;font-weight:500}

  .brand-mark{left:326px;width:40px;height:40px;border-radius:50%;background:var(--brand-green)}
  .brand-name{font-size:22px;line-height:26px;font-weight:300;color:var(--brand-green);letter-spacing:.3px}
  .label--white .brand-mark{background:var(--silver)}
  .label--white .brand-name{color:var(--silver)}
  .product-name{font-size:16px;line-height:20px;font-weight:400}
  .flavor{font-size:10px;font-weight:300}
  .muted{color:var(--muted);font-size:11.5px;font-weight:300}
  .strength{font-size:15px;line-height:19px;padding:0 7px;border-radius:8px}

  .facts{left:486px;top:18px;width:182px;background:#fff;color:#111;font-family:"Roboto Condensed",sans-serif;font-size:9px;line-height:12.5px;padding:2px 3px}
  .facts h3{font-size:15px;line-height:16px;font-weight:700}
  .facts .line{display:flex;justify-content:space-between;border-top:1.5px solid #111}
  .facts .bold{font-weight:700}
  .distributor{left:486px;width:182px;text-align:center;font-family:"Roboto Condensed",sans-serif;font-size:9.5px;line-height:13px}
  .distributor strong{font-size:10px;font-weight:700}
  .lot{left:486px;width:182px;text-align:center;font-family:"Roboto Condensed",sans-serif;font-size:9.5px;top:282px}
</style>
</head>
<body>
<div class="sheet">

  <p class="row-caption" style="left:48px;top:144px;text-align:left">4 Color or Spot Color Composite</p>

  <section class="label" style="left:392px;top:34px">
    <div class="col-left" style="top:26px"><span class="pill">SUGGESTED USE:</span></div>
    <p class="col-left body-copy" style="top:48px;padding:0 14px">Shake well before each use. Take 30 drops (1 full dropper) and place in mouth underneath tongue for 90 seconds 1-2 times daily or as recommended by a Physician.</p>
    <div class="col-left" style="top:129px"><span class="pill">WARNING:</span></div>
    <p class="col-left body-copy" style="top:151px;padding:0 14px">If you are pregnant or brestfeeding, consult a health care practitioner before using.</p>
    <div class="col-left" style="top:206px"><span class="pill pill--strong">KEEP OUT OF REACH OF CHILDREN</span></div>
    <p class="col-left caps" style="top:244px">DO NOT USE IF SEAL<br>IS BROKEN OR MISSING</p>

    <div class="col-center" style="top:11px"><span class="pill">Zero THC</span></div>
    <div class="brand-mark" style="top:52px"></div>
    <p class="col-center brand-name" style="top:124px">Marbleleaf Hemp</p>
    <p class="col-center product-name" style="top:162px">Premium - Full Spectrum<br>Hemp Oil</p>
    <p class="col-center flavor" style="top:207px">Natural Peppermint Flavor</p>
    <p class="col-center muted" style="top:232px">Dietary Supplement</p>
    <div class="col-center" style="top:256px"><span class="pill strength">2000 mg</span></div>
    <p class="col-center muted" style="top:281px">1 fl oz (30ml)</p>

    <div class="facts">
      <h3>Supplement Facts</h3>
      <p>Serving size 1ml</p>
      <p>Serving Per Container 30</p>
      <p class="line"><span class="bold">Calories 8</span><span>Calories from Fat 8</span></p>
      <p class="line bold"><span>Total Fat</span><span>1g&nbsp; 2%</span></p>
      <p class="line"><span>Full Spectrum Hemp Extract&nbsp;&nbsp; 24.99mg</span></p>
      <p class="line" style="display:block">Other Ingredients: Hemp seed oil, Grape Seed Oil, Peppermint and Stevia</p>
    </div>
    <p class="distributor" style="top:149px"><strong>DISTRIBUTED FOR:</strong><br>Greenfield Botanics, INC.<br>support@marbleleafhemp.com</p>
    <p class="lot">LOT# MRV073018TI&nbsp;&nbsp;&nbsp; Best By: 1/31/20</p>
  </section>

  <div class="divider" style="top:357px"></div>

  <p class="note note--silver" style="left:660px;top:363px;width:440px">Represents the Silver stock. Making the logo/company name<br>appear shiny almost as two seperate foil colors.</p>

  <p class="row-caption" style="left:103px;top:548px;width:200px">White Ink Layer</p>

  <section class="label label--white" style="left:392px;top:436px">
    <div class="brand-mark" style="top:47px"></div>
    <p class="col-center brand-name" style="top:124px">Marbleleaf Hemp</p>
  </section>

  <p class="note note--white" style="left:380px;top:790px;width:720px">Where White Ink will be applied. Making all art elements backed up with white ink appear with a matte finish.</p>

  <svg class="pointer" width="1200" height="1200" aria-hidden="true">
    <line x1="909" y1="414" x2="769" y2="512" stroke="#e6007e" stroke-width="1.2"/>
    <path d="M767 513 l10 -2 l-4 -6 z" fill="#e6007e"/>
    <line x1="655" y1="786" x2="582" y2="713" stroke="#00aeef" stroke-width="1.2"/>
    <path d="M580 711 l3 10 l6 -5 z" fill="#00aeef"/>
  </svg>

  <div class="divider" style="top:831px"></div>

  <p class="row-caption" style="left:59px;top:936px;width:260px;font-size:20px;line-height:25px">Reflection Rendering<br>Gradient to show effect<br>of finished product only</p>

  <section class="label" style="left:388px;top:854px">
    <div class="col-left" style="top:26px"><span class="pill">SUGGESTED USE:</span></div>
    <p class="col-left body-copy" style="top:48px;padding:0 14px">Shake well before each use. Take 30 drops (1 full dropper) and place in mouth underneath tongue for 90 seconds 1-2 times daily or as recommended by a Physician.</p>
    <div class="col-left" style="top:129px"><span class="pill">WARNING:</span></div>
    <p class="col-left body-copy" style="top:151px;padding:0 14px">If you are pregnant or brestfeeding, consult a health care practitioner before using.</p>
    <div class="col-left" style="top:206px"><span class="pill pill--strong">KEEP OUT OF REACH OF CHILDREN</span></div>
    <p class="col-left caps" style="top:244px">DO NOT USE IF SEAL<br>IS BROKEN OR MISSING</p>

    <div class="col-center" style="top:11px"><span class="pill">Zero THC</span></div>
    <div class="brand-mark" style="top:52px"></div>
    <p class="col-center brand-name" style="top:124px">Marbleleaf Hemp</p>
    <p class="col-center product-name" style="top:162px">Premium - Full Spectrum<br>Hemp Oil</p>
    <p class="col-center flavor" style="top:207px">Natural Peppermint Flavor</p>
    <p class="col-center muted" style="top:232px">Dietary Supplement</p>
    <div class="col-center" style="top:256px"><span class="pill strength">2000 mg</span></div>
    <p class="col-center muted" style="top:281px">1 fl oz (30ml)</p>

    <div class="facts">
      <h3>Supplement Facts</h3>
      <p>Serving size 1ml</p>
      <p>Serving Per Container 30</p>
      <p class="line"><span class="bold">Calories 8</span><span>Calories from Fat 8</span></p>
      <p class="line bold"><span>Total Fat</span><span>1g&nbsp; 2%</span></p>
      <p class="line"><span>Full Spectrum Hemp Extract&nbsp;&nbsp; 24.99mg</span></p>
      <p class="line" style="display:block">Other Ingredients: Hemp seed oil, Grape Seed Oil, Peppermint and Stevia</p>
    </div>
    <p class="distributor" style="top:149px"><strong>DISTRIBUTED FOR:</strong><br>Greenfield Botanics, INC.<br>support@marbleleafhemp.com</p>
    <p class="lot">LOT# MRV073018TI&nbsp;&nbsp;&nbsp; Best By: 1/31/20</p>
  </section>

</div>
</body>
</html>
```